Wordpress Theme for Tidy Meadow

Template Needs the Following:
-Main Index / home page
-Single post
-Single page
-Archives / All Articles
-Category Archives template
-Sub-Category Archives template
-Header
-Footer
Of course, must be responsive and work on all devices.
Notes on Overall Design
-Color scheme not decided, but prefer a trustworthy blue, maybe a true blue for links and accent color. Mostly black and white.
-Very similar to corvanleth.com in look, style, feel, simplicity, but will have greater focus on images in articles.
-Site is dedicated to long-form, high quality, actionable, evergreen content. This is not a news site, but it will cover a broad variety of topics. Focus on value added over timeliness / 'newness'
-Design ideas are attached as images.
Notes on Single Post Page, Header, and Footer
-For header, Title (Tidy Meadow) should be left aligned, far left
-Title can be EITHER image or text. This is a must. Clicking title name / logo should go to tidymeadow.com
-For header, 'Articles', 'About', and 'Premium' can either be center or left aligned with the border of where actual articles can go
-Footer alignment shoot match header alignment (no title needed, though)
-Title should be left aligned
-Category should be link clickable and go to category archives
Home Page / About Page / Single Page
-url is just tidymeadow.com, NOT tidymeadow.com/about
-Same layout as single page layout
-Will be text based, center aligned, very simple
-Includes site header and footer
-Title should be center aligned
-No category or author tags
Main Archives
-3 Featured articles at the top are hand selected by Tidy Meadow, NOT the 3 newest articles
-Each Main Category is shown, with a hyperlink to that category's archive page. -Clicking 'More' brings you to this archive as well
-The 3 articles for each main category are text based (no images, to save space), -They are hand selected by Tidy Meadow staff, not the most recent articles in the category
-After the category headers, all articles on the entire site are listed by date
Category Archives & Sub-Category Archives
-Same layout as main archives, but with sub-categories where the archives page had categories.
-All articles in that category listed at end of page by date
-Sub-category archives has same layout as main archive and category archive, but with nothing just our 3 favorite articles and all sub category articles by date

```html
<!DOCTYPE html>
<html lang="en">
<head>
<meta charset="utf-8">
<title>Tidy Meadow — About</title>
<link href="https://fonts.googleapis.com/css2?family=Open+Sans:wght@400;600;700&display=swap" rel="stylesheet">
<style>
:root{
  --ink:#2b2b2b;
  --text:#3c3c3c;
  --muted:#555;
  --accent:#1b7ad3;
  --accent-dark:#1565b8;
  --rule:#dcdcdc;
  --header-bg:#f3f3f3;
  --band:#232323;
  --band-text:#f2f2f2;
  --band-rule:#4a4a4a;
  --form-bg:#e3e3e3;
  --form-edge:#eeeeee;
  --white:#ffffff;
}
*{box-sizing:border-box;margin:0;padding:0}
html,body{width:799px;height:1200px;overflow:hidden;background:var(--white)}
body{position:relative;font-family:"Open Sans",Arial,sans-serif;color:var(--text)}
a{text-decoration:none;color:inherit}

.site-header{position:absolute;top:0;left:0;width:799px;height:61px;background:var(--header-bg);border-top:3px solid #3a3a3a}
.site-title{position:absolute;left:50px;top:16px;font-size:18.5px;font-weight:700;letter-spacing:.6px;color:var(--ink);text-transform:uppercase}
.main-nav{position:absolute;left:0;width:799px;top:22px;display:flex;justify-content:center;gap:0}
.main-nav a{font-size:8px;font-weight:600;letter-spacing:.3px;color:var(--ink);padding:0 12px 9px;text-transform:uppercase;position:relative}
.main-nav a.current{color:var(--accent)}
.main-nav a.current::after{content:"";position:absolute;left:1px;right:1px;bottom:0;height:2px;background:var(--accent)}

.section{position:absolute;left:0;width:799px;text-align:center}
.section-title{font-size:19px;font-weight:700;letter-spacing:.6px;text-transform:uppercase;color:var(--ink)}
.section-rule{height:1px;background:var(--rule);margin:0 auto}
.copy{width:590px;margin:0 auto;font-size:10.4px;line-height:17.3px;color:var(--text)}
.copy p+p{margin-top:9px}

.welcome{top:95px}
.welcome .section-rule{width:462px;margin-top:12px}
.welcome .copy{margin-top:27px}
.read-more{display:inline-block;margin-top:12px;font-size:10px;font-weight:700;color:var(--accent);letter-spacing:.2px}

.mission-band{position:absolute;left:0;top:350px;width:799px;height:270px}
.mission{top:388px;color:var(--band-text)}
.mission .section-title{color:var(--white)}
.mission .section-rule{width:221px;margin-top:12px;background:var(--band-rule)}
.mission .copy{margin-top:23px;color:var(--band-text);width:580px}
.mission .copy p+p{margin-top:11px}

.join{top:644px}
.join .section-rule{width:221px;margin-top:12px}
.join .copy{margin-top:22px}

.signup{position:absolute;left:228px;top:796px;width:342px;height:237px;background:var(--form-bg);border:3px solid var(--form-edge);text-align:center}
.signup-title{margin-top:21px;font-size:15.5px;font-weight:600;color:#333}
.email-field{position:absolute;left:77px;top:73px;width:184px;height:28px;background:var(--white);border:1px solid #cfcfcf}
.human-check{position:absolute;left:77px;top:107px;width:184px;height:50px;background:#f9f9f9;border:1px solid #d3d3d3;border-radius:2px;text-align:left}
.human-check .box{position:absolute;left:6px;top:14px;width:17px;height:17px;background:var(--white);border:2px solid #c1c1c1;border-radius:2px}
.human-check .label{position:absolute;left:30px;top:17px;font-size:8px;color:#222}
.human-check .mark{position:absolute;right:14px;top:6px;width:18px;height:18px;border-radius:50%;background:#a9b8d6}
.human-check .brand{position:absolute;right:8px;top:30px;font-size:5px;color:#666;text-align:center;line-height:8px}
.submit{position:absolute;left:77px;top:162px;width:184px;height:28px;border-radius:2px;background:linear-gradient(#2a86dc,var(--accent-dark));color:var(--white);font-size:10.5px;font-weight:700;letter-spacing:.6px;line-height:28px;text-transform:uppercase}
.signup-note{position:absolute;left:0;width:100%;top:204px;font-size:6.6px;color:#444;letter-spacing:.2px}

.site-footer{position:absolute;left:0;top:1080px;width:799px;height:120px;background:var(--header-bg);border-top:2px solid #3a3a3a;text-align:center}
.footer-nav{margin-top:38px;display:flex;justify-content:center}
.footer-nav a{font-size:8px;font-weight:600;color:var(--ink);padding:0 12px;text-transform:uppercase}
.footer-legal{margin-top:9px;font-size:8px;color:var(--muted);line-height:14px}
.footer-legal .sep{padding:0 6px}
</style>
</head>
<body>

<header class="site-header">
  <a class="site-title" href="https://tidymeadow.com">Tidy Meadow</a>
  <nav class="main-nav">
    <a href="#">Articles</a>
    <a href="#" class="current">About</a>
    <a href="#">Premium</a>
  </nav>
</header>

<section class="section welcome">
  <h1 class="section-title">Welcome to Tidy Meadow</h1>
  <div class="section-rule"></div>
  <div class="copy">
    <p>Aliquam molestie, mi et imperdiet euismod, dui purus auctor tellus, et interdum lacus lectus et ante. Sed accumsan sollicitudin sapien, sit amet adipiscing turpis gravida ac. In congue, neque ac lobortis volutpat, libero mauris varius mi, vitae suscipit ipsum ligula vitae risus. Duis aliquam nibh a dui iaculis viverra id a velit. Vivamus egestas risus in magna varius commodo. Sed semper viverra egestas. Etiam pretium porttitor lectus, vel ornare neque porta volutpat.</p>
    <p>Aliquam molestie, mi et imperdiet euismod, dui purus auctor tellus, et interdum lacus lectus et ante. Sed accumsan sollicitudin sapien, sit amet adipiscing turpis gravida ac. In congue, neque ac lobortis volutpat, libero mauris varius mi, vitae suscipit ipsum ligula vitae risus. Duis aliquam nibh a dui iaculis viverra id a velit.</p>
  </div>
  <a class="read-more" href="#">Read Full Story</a>
</section>

<svg class="mission-band" viewBox="0 0 799 270" preserveAspectRatio="none" aria-hidden="true">
  <polygon points="0,0 400,18 799,0 799,270 400,251 0,270" fill="#232323"/>
</svg>

<section class="section mission">
  <h2 class="section-title">The Mission</h2>
  <div class="section-rule"></div>
  <div class="copy">
    <p>Aliquam molestie, mi et imperdiet euismod, dui purus auctor tellus, et interdum lacus lectus et ante. Sed accumsan sollicitudin sapien, sit amet adipiscing turpis gravida ac. In congue, neque ac lobortis volutpat, libero mauris varius mi, vitae suscipit ipsum ligula vitae risus. Duis aliquam nibh a dui iaculis viverra id a velit. Vivamus egestas risus in magna varius commodo. Sed semper viverra egestas.</p>
    <p>Aliquam molestie, mi et imperdiet euismod, dui purus auctor tellus, et interdum lacus lectus et ante. Sed accumsan sollicitudin sapien, sit amet adipiscing turpis gravida ac. In congue, neque ac lobortis volutpat, libero mauris varius mi, vitae suscipit ipsum ligula vitae risus. Duis aliquam nibh a dui iaculis viverra id a velit.</p>
  </div>
</section>

<section class="section join">
  <h2 class="section-title">Join Us Now</h2>
  <div class="section-rule"></div>
  <div class="copy">
    <p>Aliquam molestie, mi et imperdiet euismod, dui purus auctor tellus, et interdum lacus lectus et ante. Sed accumsan sollicitudin sapien, sit amet adipiscing turpis gravida ac. In congue, neque ac lobortis volutpat, libero mauris varius mi, vitae suscipit ipsum ligula vitae risus. Duis aliquam nibh a dui iaculis viverra id a velit. Vivamus egestas risus in magna varius commodo. Sed semper viverra egestas. Etiam pretium porttitor lectus, vel ornare neque porta volutpat.</p>
  </div>
</section>

<form class="signup">
  <h3 class="signup-title">My Email Address is...</h3>
  <div class="email-field"></div>
  <div class="human-check">
    <span class="box"></span>
    <span class="label">I'm not a robot</span>
    <span class="mark"></span>
    <span class="brand">HumanCheck<br>Privacy - Terms</span>
  </div>
  <div class="submit">Get Updates</div>
  <p class="signup-note">Zero spam. Unsubscribe any time.</p>
</form>

<footer class="site-footer">
  <nav class="footer-nav">
    <a href="#">Articles</a>
    <a href="#">About</a>
    <a href="#">Premium</a>
  </nav>
  <div class="footer-legal">
    <div>Copyright © 2017. Company Name. All Right Reserved</div>
    <div><a href="#">Contact</a><span class="sep">|</span><a href="#">Disclaimer</a></div>
  </div>
</footer>

</body>
</html>
```